Venlow Partners
Global Real Estate Investing
Venlow Partners -
Creative Brief
Modern
Ravi Talbert
President
24817 Mobley Lane 2nd Floor Southgate MI 48195
rtalbert@venlowpartners.example
www.venlowpartners.example

```html
<!DOCTYPE html>
<html lang="en">
<head>
<meta charset="utf-8">
<title>Venlow Partners – Business Cards</title>
<link rel="stylesheet" href="https://fonts.googleapis.com/css2?family=Open+Sans:wght@400;700&display=swap">
<style>
  :root {
    --page: #e9e9ec;
    --card-top: #ffffff;
    --card-bottom: #eceef3;
    --brand: #2a3a8f;
    --ink: #2b2b2f;
  }
  * { margin: 0; padding: 0; box-sizing: border-box; }
  html, body { width: 1200px; height: 915px; overflow: hidden; }
  body {
    background: var(--page);
    font-family: "Open Sans", Arial, sans-serif;
    position: relative;
  }
  .card {
    position: absolute;
    width: 600px;
    height: 345px;
    border-radius: 22px;
    background: linear-gradient(180deg, var(--card-top) 0%, var(--card-bottom) 100%);
    box-shadow: 0 6px 18px rgba(0,0,0,0.18);
    overflow: hidden;
  }
  .card--front { left: 69px; top: 54px; }
  .card--back { left: 505px; top: 468px; }
  .brand {
    position: absolute;
    display: flex;
    flex-direction: column;
    align-items: center;
    color: var(--brand);
    font-size: 30px;
    font-weight: 700;
    text-transform: uppercase;
    text-align: center;
    line-height: 1.1;
  }
  .brand__dot {
    width: 96px;
    height: 96px;
    border-radius: 50%;
    background: var(--brand);
    margin-bottom: 14px;
  }
  .card--front .brand { left: 40px; top: 95px; width: 230px; }
  .card--back .brand { left: 185px; top: 87px; width: 230px; }
  .contact {
    position: absolute;
    left: 325px;
    top: 58px;
    color: var(--ink);
    font-size: 15px;
    line-height: 1.45;
  }
  .contact__name { color: var(--brand); font-size: 26px; font-weight: 700; text-transform: uppercase; line-height: 1.15; }
  .contact__title { font-size: 16px; font-weight: 700; text-transform: uppercase; margin-bottom: 16px; }
  .contact__address { margin-bottom: 16px; }
  .contact__label { font-weight: 700; }
  .contact__web { font-weight: 700; }
</style>
</head>
<body>
  <section class="card card--front">
    <div class="brand">
      <span class="brand__dot"></span>
      <span>Venlow<br>Partners</span>
    </div>
    <div class="contact">
      <p class="contact__name">Ravi Talbert</p>
      <p class="contact__title">President</p>
      <p class="contact__address">24817 Mobley Lane<br>2nd Floor<br>Southgate MI 48195</p>
      <p><span class="contact__label">P:</span> 555-014-2290</p>
      <p><span class="contact__label">F:</span> 555-014-2290</p>
      <p><span class="contact__label">E:</span> rtalbert@venlowpartners.example</p>
      <p class="contact__web">www.venlowpartners.example</p>
    </div>
  </section>

  <section class="card card--back">
    <div class="brand">
      <span class="brand__dot"></span>
      <span>Venlow<br>Partners</span>
    </div>
  </section>
</body>
</html>
```